Exciting new Aussie social network app - designer wanted!

Interested in this entire Freelance Job?
Here is the full project link:
http://jobs.pixelquarry.com.au/job.aspx?id=582716
****
We are a startup based in Melbourne working on a hot new iOS/Android social media app with an edge.
We have completed the scoping phase with the app developers and we are currently seeking a talented app UI/UX designer to work with to create something highly polished.
Our aim with this competition is to mockup the first screen of our app and effectively meet the designer we would love to move forward with to complete the entire design phase after a full debrief. Our app will be comparable to the look/feel of the Quillmoss or Glimmerdot apps, however, the functionality will be a little different. One of our app's main features does involve sharing smartphone captured photos to a stream (stylised gallery of photos) on a network.
We are inspired by the design language of the following iOS apps:
Quillmoss
https://apps.velmora.example/au/app/quillmoss/id813560274?mt=8
Barvo
https://apps.velmora.example/au/app/barvo/id690134827?mt=8
Hoxwelt
https://apps.velmora.example/au/app/hoxwelt/id731842056?mt=8
Lumbrazet
https://apps.velmora.example/au/app/lumbrazet/id572019386?mt=8
Please refer to the screenshot attached entitled MAIN SCREEN and create your own version of this UI/UX for this competition.
Our requirements -
* The title at the top title bar is called "Zorvy"
* the 5 navigation text & buttons at the bottom dock from left to right are:
FEED (Icon of a map pin drop), PEOPLE (Icon of 3 people), CAMERA graphic or a PLUS (+) symbol or both without text label, ACTIVITY(chat boxes/hearts), ME (Icon of Person)
* We need to see what the dock items would like like in each of the 5 states. Eg. What would it look like then the FEED state is highlighted when the user is in the feed section of the app.
* Screen to display whether you are following these users or displaying content from all users.
* We want a small text overlay over each image in the corner, perhaps semi-transparent, to show a 3-4 character code and a heart symbol to like the image.
* We need to see at least 1 new notification any of the dock items
Please refer to attached files for further illustration of buttons we have considered.
Thank you very much for your effort!
We look forward to your mockup and hopefully further work together!
If you are interested in this entire job check out our link to the full freelance project:
Target Market(s)
18-35 years, we expect a more female user demographic, but want to appeal to both sexes.
Industry/Entity Type
Camera
Look and feel

```html
<!DOCTYPE html>
<html lang="en">
<head>
<meta charset="utf-8">
<title>Zorvy – All Users Stream</title>
<link rel="stylesheet" href="https://fonts.googleapis.com/css2?family=Raleway:wght@300&family=Roboto:wght@400;500;700&display=swap">
<style>
  :root {
    --wood-light: #e2c7a0;
    --wood-mid: #d6b68a;
    --wood-dark: #b88f62;
    --dock-top: #c9a27a;
    --dock-bottom: #a77f56;
    --ink: #2b2118;
    --white: #ffffff;
    --seg-tan: #c8a678;
    --seg-tan-dark: #a9865a;
    --seg-blue: #3b8fe0;
    --seg-blue-dark: #1f6bc2;
    --like-blue: #3f93e6;
    --heart-grey: #8d8a86;
    --badge-red: #d8322b;
    --code-bg: rgba(40, 30, 22, 0.65);
  }
  * { box-sizing: border-box; margin: 0; padding: 0; }
  html, body { width: 677px; height: 1200px; overflow: hidden; }
  body {
    position: relative;
    font-family: "Roboto", Arial, sans-serif;
    background: linear-gradient(90deg, var(--wood-mid), var(--wood-light) 30%, var(--wood-mid) 55%, var(--wood-light) 80%, var(--wood-mid));
    color: var(--ink);
  }

  /* status bar */
  .status-bar {
    position: absolute; left: 0; top: 0; width: 677px; height: 45px;
    display: flex; align-items: center; justify-content: space-between;
    padding: 0 14px; font-size: 26px; font-weight: 500; color: var(--ink);
  }
  .status-left, .status-right { display: flex; align-items: center; gap: 10px; width: 200px; }
  .status-right { justify-content: flex-end; }
  .status-time { font-weight: 700; }

  /* title bar */
  .title-bar { position: absolute; left: 0; top: 45px; width: 677px; height: 95px; }
  .back-button {
    position: absolute; left: 14px; top: 18px; width: 104px; height: 50px;
    display: flex; align-items: center; justify-content: flex-end; padding-right: 14px;
    font-size: 24px; color: #5a4632;
    background: linear-gradient(#efdcc0, #d4b48a);
    border: 2px solid #a98459;
    border-radius: 10px;
    clip-path: polygon(22px 0, 100% 0, 100% 100%, 22px 100%, 0 50%);
  }
  .app-title {
    position: absolute; left: 0; right: 0; top: 8px; text-align: center;
    font-family: "Raleway", "Helvetica Neue", sans-serif; font-weight: 300;
    font-size: 70px; color: var(--white); letter-spacing: 1px;
    text-shadow: 0 2px 3px rgba(90, 60, 30, 0.45);
  }

  /* segmented control */
  .audience-toggle {
    position: absolute; left: 162px; top: 190px; width: 380px; height: 54px;
    display: flex; border: 2px solid #8a6a45; border-radius: 10px; overflow: hidden;
    box-shadow: 0 2px 3px rgba(0,0,0,0.25);
  }
  .toggle-option {
    flex: 1; display: flex; align-items: center; justify-content: center;
    font-size: 25px; font-weight: 500;
  }
  .toggle-option.is-idle {
    background: linear-gradient(var(--seg-tan), var(--seg-tan-dark)); color: var(--ink);
    border-right: 2px solid #8a6a45;
  }
  .toggle-option.is-active {
    background: linear-gradient(#5aa7ec, var(--seg-blue) 50%, var(--seg-blue-dark)); color: var(--white);
  }

  /* photo stream */
  .photo-stream {
    position: absolute; left: 18px; top: 298px;
    display: grid; grid-template-columns: repeat(3, 194px); grid-auto-rows: 172px;
    column-gap: 27px; row-gap: 19px;
  }
  .photo-tile {
    position: relative; background: var(--white); padding: 7px;
    box-shadow: 0 2px 5px rgba(60, 40, 20, 0.4);
  }
  .photo-fill { width: 100%; height: 100%; }
  .photo-fill.cool { background: linear-gradient(160deg, #c9c4bd, #f2f1ee 45%, #d8d4cc 70%, #9e9a92); }
  .photo-fill.warm { background: linear-gradient(160deg, #efe4cf, #c9a378 45%, #7a4a2c 75%, #b58b62); }
  .photo-fill.bright { background: linear-gradient(160deg, #f3ead8, #d9bf95 45%, #8e5e3a 75%, #cfae82); }
  .code-tag {
    position: absolute; left: 7px; bottom: 7px; padding: 3px 8px;
    background: var(--code-bg); color: var(--white); font-size: 13px; font-weight: 700; letter-spacing: 0.5px;
  }
  .like-heart { position: absolute; right: 10px; top: 10px; width: 34px; height: 30px; }
  .liked-corner { position: absolute; right: 0; top: 0; width: 62px; height: 62px; }

  /* dock */
  .dock {
    position: absolute; left: 0; top: 1079px; width: 677px; height: 121px;
    background: linear-gradient(var(--dock-top), var(--dock-bottom));
    border-top: 2px solid #8f6b45;
    display: grid; grid-template-columns: 1fr 1fr 130px 1fr 1fr; align-items: end;
  }
  .dock-item {
    display: flex; flex-direction: column; align-items: center; gap: 6px; padding-bottom: 12px;
    font-size: 26px; font-weight: 500; color: var(--white);
    text-shadow: 0 1px 2px rgba(60, 35, 15, 0.6);
  }
  .dock-item svg { width: 52px; height: 52px; }
  .camera-button {
    position: relative; align-self: stretch; margin-top: -16px;
    background: linear-gradient(#d8b58b, #a9825a);
    border: 2px solid #8f6b45; border-bottom: none; border-radius: 14px 14px 0 0;
    display: flex; align-items: center; justify-content: center;
  }
  .camera-button svg { width: 74px; height: 62px; }
  .badge {
    position: absolute; right: 18px; top: 14px; min-width: 40px; height: 40px; padding: 0 6px;
    border-radius: 20px; background: var(--badge-red); border: 3px solid var(--white);
    color: var(--white); font-size: 20px; font-weight: 700;
    display: flex; align-items: center; justify-content: center;
  }
</style>
</head>
<body>

<header class="status-bar">
  <div class="status-left">
    <svg width="50" height="14" viewBox="0 0 50 14"><g fill="#2b2118"><circle cx="5" cy="7" r="4.5"/><circle cx="15" cy="7" r="4.5"/><circle cx="25" cy="7" r="4.5"/><circle cx="35" cy="7" r="4.5"/><circle cx="45" cy="7" r="4.5" fill="none" stroke="#2b2118" stroke-width="1.5"/></g></svg>
    <span>Vantor</span>
    <svg width="26" height="20" viewBox="0 0 26 20"><g fill="none" stroke="#2b2118" stroke-width="3" stroke-linecap="round"><path d="M2 7a16 16 0 0 1 22 0"/><path d="M6 11a10 10 0 0 1 14 0"/></g><circle cx="13" cy="16" r="2.5" fill="#2b2118"/></svg>
  </div>
  <span class="status-time">11:11 AM</span>
  <div class="status-right">
    <svg width="18" height="20" viewBox="0 0 18 20"><rect x="3" y="8" width="12" height="10" rx="1.5" fill="#2b2118"/><path d="M5.5 8V5a3.5 3.5 0 0 1 7 0v3" fill="none" stroke="#2b2118" stroke-width="2.2"/></svg>
    <svg width="16" height="20" viewBox="0 0 16 20"><path d="M15 1 1 9l6 2 2 8z" fill="#2b2118"/></svg>
    <svg width="52" height="22" viewBox="0 0 52 22"><rect x="1" y="1" width="44" height="20" rx="3" fill="none" stroke="#2b2118" stroke-width="2"/><rect x="4" y="4" width="38" height="14" rx="1.5" fill="#2b2118"/><rect x="46" y="7" width="4" height="8" rx="1" fill="#2b2118"/></svg>
  </div>
</header>

<nav class="title-bar">
  <div class="back-button">Back</div>
  <h1 class="app-title">Zorvy</h1>
</nav>

<div class="audience-toggle">
  <div class="toggle-option is-idle">Following</div>
  <div class="toggle-option is-active">All Users</div>
</div>

<main class="photo-stream">
  <!-- row 1 -->
  <article class="photo-tile"><div class="photo-fill cool" role="img" aria-label="Shared photo of a white kitchen"></div><span class="code-tag">CODE</span>
    <svg class="like-heart" viewBox="0 0 34 30"><path d="M17 29 3 15A8 8 0 0 1 17 5a8 8 0 0 1 14 10z" fill="var(--heart-grey)" stroke="#fff" stroke-width="2"/></svg></article>
  <article class="photo-tile"><div class="photo-fill warm" role="img" aria-label="Shared photo of a warm timber kitchen"></div><span class="code-tag">CODE</span>
    <svg class="liked-corner" viewBox="0 0 62 62"><path d="M0 0h62v62z" fill="var(--like-blue)"/><path d="M44 30 34 20a5.5 5.5 0 0 1 10-6a5.5 5.5 0 0 1 10 6z" fill="#fff"/></svg></article>
  <article class="photo-tile"><div class="photo-fill bright" role="img" aria-label="Shared photo of a kitchen with island bench"></div><span class="code-tag">CODE</span>
    <svg class="like-heart" viewBox="0 0 34 30"><path d="M17 29 3 15A8 8 0 0 1 17 5a8 8 0 0 1 14 10z" fill="var(--heart-grey)" stroke="#fff" stroke-width="2"/></svg></article>
  <!-- row 2 -->
  <article class="photo-tile"><div class="photo-fill cool" role="img" aria-label="Shared photo of a white kitchen"></div><span class="code-tag">CODE</span>
    <svg class="liked-corner" viewBox="0 0 62 62"><path d="M0 0h62v62z" fill="var(--like-blue)"/><path d="M44 30 34 20a5.5 5.5 0 0 1 10-6a5.5 5.5 0 0 1 10 6z" fill="#fff"/></svg></article>
  <article class="photo-tile"><div class="photo-fill warm" role="img" aria-label="Shared photo of a warm timber kitchen"></div><span class="code-tag">CODE</span>
    <svg class="like-heart" viewBox="0 0 34 30"><path d="M17 29 3 15A8 8 0 0 1 17 5a8 8 0 0 1 14 10z" fill="var(--heart-grey)" stroke="#fff" stroke-width="2"/></svg></article>
  <article class="photo-tile"><div class="photo-fill bright" role="img" aria-label="Shared photo of a kitchen with island bench"></div><span class="code-tag">CODE</span>
    <svg class="like-heart" viewBox="0 0 34 30"><path d="M17 29 3 15A8 8 0 0 1 17 5a8 8 0 0 1 14 10z" fill="var(--heart-grey)" stroke="#fff" stroke-width="2"/></svg></article>
  <!-- row 3 -->
  <article class="photo-tile"><div class="photo-fill cool" role="img" aria-label="Shared photo of a white kitchen"></div><span class="code-tag">CODE</span>
    <svg class="like-heart" viewBox="0 0 34 30"><path d="M17 29 3 15A8 8 0 0 1 17 5a8 8 0 0 1 14 10z" fill="var(--heart-grey)" stroke="#fff" stroke-width="2"/></svg></article>
  <article class="photo-tile"><div class="photo-fill warm" role="img" aria-label="Shared photo of a warm timber kitchen"></div><span class="code-tag">CODE</span>
    <svg class="like-heart" viewBox="0 0 34 30"><path d="M17 29 3 15A8 8 0 0 1 17 5a8 8 0 0 1 14 10z" fill="var(--heart-grey)" stroke="#fff" stroke-width="2"/></svg></article>
  <article class="photo-tile"><div class="photo-fill bright" role="img" aria-label="Shared photo of a kitchen with island bench"></div><span class="code-tag">CODE</span>
    <svg class="like-heart" viewBox="0 0 34 30"><path d="M17 29 3 15A8 8 0 0 1 17 5a8 8 0 0 1 14 10z" fill="var(--heart-grey)" stroke="#fff" stroke-width="2"/></svg></article>
  <!-- row 4 -->
  <article class="photo-tile"><div class="photo-fill cool" role="img" aria-label="Shared photo of a white kitchen"></div><span class="code-tag">CODE</span>
    <svg class="liked-corner" viewBox="0 0 62 62"><path d="M0 0h62v62z" fill="var(--like-blue)"/><path d="M44 30 34 20a5.5 5.5 0 0 1 10-6a5.5 5.5 0 0 1 10 6z" fill="#fff"/></svg></article>
  <article class="photo-tile"><div class="photo-fill warm" role="img" aria-label="Shared photo of a warm timber kitchen"></div><span class="code-tag">CODE</span>
    <svg class="like-heart" viewBox="0 0 34 30"><path d="M17 29 3 15A8 8 0 0 1 17 5a8 8 0 0 1 14 10z" fill="var(--heart-grey)" stroke="#fff" stroke-width="2"/></svg></article>
  <article class="photo-tile"><div class="photo-fill bright" role="img" aria-label="Shared photo of a kitchen with island bench"></div><span class="code-tag">CODE</span>
    <svg class="liked-corner" viewBox="0 0 62 62"><path d="M0 0h62v62z" fill="var(--like-blue)"/><path d="M44 30 34 20a5.5 5.5 0 0 1 10-6a5.5 5.5 0 0 1 10 6z" fill="#fff"/></svg></article>
</main>

<footer class="dock">
  <div class="dock-item">
    <svg viewBox="0 0 52 52"><path d="M26 4a15 15 0 0 0-15 15c0 11 15 29 15 29s15-18 15-29A15 15 0 0 0 26 4z" fill="#6b4c30"/><circle cx="26" cy="19" r="6" fill="var(--dock-top)"/></svg>
    <span>Feed</span>
  </div>
  <div class="dock-item">
    <svg viewBox="0 0 52 52"><g fill="#6b4c30"><circle cx="13" cy="18" r="6"/><circle cx="39" cy="18" r="6"/><path d="M2 42c0-9 5-14 11-14s11 5 11 14z"/><path d="M28 42c0-9 5-14 11-14s11 5 11 14z"/><circle cx="26" cy="15" r="8"/><path d="M12 46c0-12 6-19 14-19s14 7 14 19z" stroke="var(--dock-top)" stroke-width="2"/></g></svg>
    <span>People</span>
  </div>
  <div class="camera-button">
    <svg viewBox="0 0 74 62"><path d="M8 14h14l5-8h20l5 8h14a4 4 0 0 1 4 4v36a4 4 0 0 1-4 4H8a4 4 0 0 1-4-4V18a4 4 0 0 1 4-4z" fill="#5a3f27"/><circle cx="37" cy="35" r="14" fill="var(--dock-top)"/><circle cx="37" cy="35" r="9" fill="#5a3f27"/></svg>
    <span class="badge">56</span>
  </div>
  <div class="dock-item">
    <svg viewBox="0 0 52 52"><g fill="#6b4c30"><path d="M4 8h28a3 3 0 0 1 3 3v16a3 3 0 0 1-3 3H16l-8 7v-7H4a3 3 0 0 1-3-3V11a3 3 0 0 1 3-3z"/><path d="M38 18h10a3 3 0 0 1 3 3v15a3 3 0 0 1-3 3h-3v7l-8-7H22a3 3 0 0 1-3-3v-3h13a6 6 0 0 0 6-6z"/></g><path d="M18 25l-6-6a3.2 3.2 0 0 1 6-3a3.2 3.2 0 0 1 6 3z" fill="var(--dock-top)"/></svg>
    <span>Activity</span>
  </div>
  <div class="dock-item">
    <svg viewBox="0 0 52 52"><g fill="#6b4c30"><circle cx="26" cy="15" r="10"/><path d="M8 48c0-14 8-22 18-22s18 8 18 22z"/></g></svg>
    <span>Me</span>
  </div>
</footer>

</body>
</html>
```